依頼詳細
小学校経由で小学生の皆さんに、チラシを配布いたします。加東市、岬野市教育委員会の後援もとっており、夏休みの宿題対策ワークショップをするどのショッピングセンターよりも選んでいただける、楽しい見栄えの作品になればうれしいです。
記載項目
詳細は添付ファイルにて
サイズ
A4
ページ数
片面
希望イメージ
シンプル 複雑
単色 カラフル
暗い 明るい
日常 高級
遊び心 厳粛
未来的 伝統的
女性的 男性的
希望する色
黄・オレンジ系、青系、水色系
納品ファイル
• 高解像度JPG (.jpg)
• イラストレーター形式 (.ai)
• PNG形式 (.png)
補足説明
■ 選んだ理由

表面のみという表現場所で、内容がみやすく、かつ 大変華やかで
子ども達の目を引くデザインになっているところや、写真のロゴからの抽出で
うまく取り入れていただいたり、気の利いた内容でした

■ 提案者全員のお礼・コメント

たくさんのご応募いただき、まことにありがとうございました。
また、同じくコンペ形式でお世話になると思いますが、ぜひまたご提案ください。
よろしくお願いいたします。

```html
<!DOCTYPE html>
<html lang="ja">
<head>
<meta charset="utf-8">
<title>夏休み 宿題対策ワークショップ</title>
<link href="https://fonts.googleapis.com/css2?family=Mochiy+Pop+One&family=M+PLUS+Rounded+1c:wght@500;700;800&display=swap" rel="stylesheet">
<style>
:root{
  --sun:#ffe94a;
  --sun-pale:#fff7b8;
  --sky:#1a8fd8;
  --sky-deep:#1769b8;
  --aqua:#bfe8fa;
  --red:#e8343a;
  --orange:#f39a1e;
  --green:#2fa86a;
  --ink:#333;
  --white:#fff;
}
*{box-sizing:border-box;margin:0;padding:0}
html,body{width:846px;height:1200px;overflow:hidden}
body{font-family:"M PLUS Rounded 1c",sans-serif;color:var(--ink);background:var(--sun)}
.flyer{position:relative;width:846px;height:1200px;background:linear-gradient(var(--sun-pale) 0,var(--sun) 380px);overflow:hidden}
.kid-art{position:absolute;top:20px;width:170px;height:180px;border-radius:24px;background:linear-gradient(160deg,#ffd1a8,#8cc8f0)}
.kid-art.left{left:22px}
.kid-art.right{right:22px;background:linear-gradient(200deg,#ffd1a8,#f6a0b0)}
.headline{position:absolute;top:10px;left:0;width:100%;text-align:center;font-family:"Mochiy Pop One",sans-serif}
.headline .summer{font-size:76px;color:var(--sky);line-height:1.05;letter-spacing:4px;-webkit-text-stroke:2px var(--white);paint-order:stroke fill;text-shadow:0 4px 0 var(--sky-deep)}
.headline .event{display:inline-block;margin:4px 0 2px;padding:2px 22px;background:var(--sky);color:var(--white);font-size:28px;border-radius:8px}
.headline .homework{font-size:66px;color:var(--red);line-height:1.1;letter-spacing:6px;-webkit-text-stroke:2px var(--white);paint-order:stroke fill;text-shadow:0 4px 0 #a51d22}
.dates{position:absolute;top:202px;width:100%;text-align:center;font-family:"Mochiy Pop One",sans-serif;color:var(--red);font-size:50px;line-height:70px;letter-spacing:1px}
.dates small{font-size:30px}
.hours{position:absolute;top:272px;width:100%;text-align:center;font-size:15px;font-weight:700}
.venue{position:absolute;top:298px;left:40px;width:766px;height:82px;display:flex;background:var(--white);border:3px solid var(--green);border-radius:12px;overflow:hidden}
.venue .label{width:150px;background:var(--green);color:var(--white);font-weight:800;font-size:24px;display:flex;align-items:center;justify-content:center}
.venue .detail{padding:10px 20px}
.venue .place{font-size:25px;font-weight:800;color:var(--green)}
.venue .place small{font-size:15px}
.venue .address{font-size:15px;font-weight:700}
.facts{position:absolute;top:392px;left:40px;width:766px;display:flex;gap:14px}
.fact{flex:1;background:var(--white);border-radius:12px;overflow:hidden;height:122px;border:3px solid var(--orange)}
.fact h3{background:var(--orange);color:var(--white);text-align:center;font-size:22px;padding:4px 0}
.fact p{text-align:center;font-size:16px;font-weight:700;padding:8px 8px 0;line-height:1.35}
.fact .note{font-size:12px;font-weight:500;padding-top:4px}
.menu{position:absolute;top:528px;left:28px;width:790px;background:var(--aqua);border-radius:14px;padding:0 12px 12px}
.menu h2{background:var(--sky);color:var(--white);font-size:24px;padding:5px 20px;margin:0 -12px 10px;border-radius:14px 14px 0 0;letter-spacing:2px}
.day{display:flex;background:var(--white);border-radius:10px;height:136px;margin-bottom:8px;overflow:hidden}
.day.d31{height:150px;margin-bottom:0}
.day .list{width:290px;padding:0 12px 8px}
.day .tab{display:inline-block;color:var(--white);font-family:"Mochiy Pop One",sans-serif;font-size:22px;padding:2px 14px;border-radius:0 0 10px 10px;margin-bottom:6px}
.day .tab small{font-size:14px;font-family:"M PLUS Rounded 1c",sans-serif;font-weight:700}
.day.d29 .tab{background:var(--red)}
.day.d30 .tab{background:var(--orange)}
.day.d31 .tab{background:var(--sky)}
.day ul{list-style:none}
.day li{display:flex;justify-content:space-between;font-size:15px;font-weight:700;border-bottom:1px dashed #bbb;padding:2px 0}
.day li span:last-child{color:var(--red)}
.day .photos{flex:1;display:flex;gap:8px;padding:10px 10px 10px 0}
.photo{flex:1;border-radius:6px}
.contact{position:absolute;top:1060px;left:40px;width:460px}
.contact .lead{display:flex;align-items:center;gap:8px;font-size:17px;font-weight:800}
.contact .mail{margin-top:6px;font-family:"Mochiy Pop One",sans-serif;font-size:33px;line-height:1.2;color:var(--sky-deep);white-space:nowrap}
.organizers{position:absolute;top:1064px;left:530px;width:290px;font-size:11px;font-weight:700;line-height:1.55}
.brand{margin-top:8px;display:flex;align-items:center;gap:8px;font-size:24px;font-weight:800;color:var(--sky-deep)}
.brand i{width:18px;height:18px;border-radius:50%;background:var(--sky-deep)}
</style>
</head>
<body>
<main class="flyer">
  <div class="kid-art left" role="img" aria-label="工作をする子どものイラスト"></div>
  <div class="kid-art right" role="img" aria-label="工作を楽しむ子どものイラスト"></div>

  <header class="headline">
    <div class="summer">夏休み</div>
    <div class="event">ワークショップ開催</div>
    <div class="homework">宿題対策</div>
  </header>

  <p class="dates">7/29<small>(金)</small>・30<small>(土)</small>・31<small>(日)</small></p>
  <p class="hours">午前10時30分〜午後4時ごろまで ※整理券がなくなり次第終了</p>

  <section class="venue">
    <div class="label">開催場所</div>
    <div class="detail">
      <div class="place">みさきショッピングパークLumo内 <small>セントラルコート</small></div>
      <div class="address">〒679-0000 兵庫県岬野市中町2-14-5</div>
    </div>
  </section>

  <section class="facts">
    <div class="fact"><h3>参加費</h3><p>おひとり様1種類300円〜</p><p class="note">※工作内容等、材料があれば<br>別途参加料</p></div>
    <div class="fact"><h3>整理券配布</h3><p>各日、10時から<br>セントラルコートにて<br>配布いたします</p></div>
    <div class="fact"><h3>定員</h3><p>1回15家族様</p><p class="note">※満席の場合は<br>ご容赦ください</p></div>
  </section>

  <section class="menu">
    <h2>ワークショップメニュー</h2>
    <div class="day d29">
      <div class="list">
        <span class="tab">7/29<small>(金)</small></span>
        <ul>
          <li><span>①オリジナル傘を作ろう</span><span>300円</span></li>
          <li><span>②コロコロガーレ</span><span>300円</span></li>
          <li><span>③スクラッチアート</span><span>300円</span></li>
        </ul>
      </div>
      <div class="photos">
        <div class="photo" role="img" aria-label="オリジナル傘の作品写真" style="background:linear-gradient(#9fd3f2,#5aa7d8)"></div>
        <div class="photo" role="img" aria-label="コロコロガーレの作品写真" style="background:linear-gradient(#f4d39a,#d9a25c)"></div>
        <div class="photo" role="img" aria-label="スクラッチアートの作品写真" style="background:linear-gradient(#3c3c5a,#8a5cc0)"></div>
      </div>
    </div>
    <div class="day d30">
      <div class="list">
        <span class="tab">7/30<small>(土)</small></span>
        <ul>
          <li><span>①ペットボトルドレス貯金箱</span><span>300円</span></li>
          <li><span>②ひまわりリース</span><span>300円</span></li>
          <li><span>③風鈴を作ろう</span><span>300円</span></li>
        </ul>
      </div>
      <div class="photos">
        <div class="photo" role="img" aria-label="ペットボトル貯金箱の作品写真" style="background:linear-gradient(#f6c6d8,#e383a8)"></div>
        <div class="photo" role="img" aria-label="ひまわりリースの作品写真" style="background:linear-gradient(#ffe36a,#f0a020)"></div>
        <div class="photo" role="img" aria-label="風鈴の作品写真" style="background:linear-gradient(#d8f0fb,#7fc4e8)"></div>
      </div>
    </div>
    <div class="day d31">
      <div class="list">
        <span class="tab">7/31<small>(日)</small></span>
        <ul>
          <li><span>①和紙ランタンを作ろう</span><span>300円</span></li>
          <li><span>②折り紙アート</span><span>200円</span></li>
          <li><span>③牛乳パックで工作</span><span>300円</span></li>
          <li><span>④くるくるランド</span><span>300円</span></li>
        </ul>
      </div>
      <div class="photos">
        <div class="photo" role="img" aria-label="和紙ランタンの作品写真" style="background:linear-gradient(#fbe7c0,#e8b86a)"></div>
        <div class="photo" role="img" aria-label="折り紙アートの作品写真" style="background:linear-gradient(#f7b8a8,#e2604a)"></div>
        <div class="photo" role="img" aria-label="牛乳パック工作の作品写真" style="background:linear-gradient(#e8f4e0,#9ccc7a)"></div>
        <div class="photo" role="img" aria-label="くるくるランドの作品写真" style="background:linear-gradient(#d9d2f2,#8f7fd0)"></div>
      </div>
    </div>
  </section>

  <footer>
    <div class="contact">
      <p class="lead">
        <svg width="30" height="22" viewBox="0 0 30 22" aria-hidden="true"><rect x="1" y="1" width="28" height="20" rx="3" fill="#1769b8"/><path d="M2 3 L15 13 L28 3" stroke="#fff" stroke-width="2" fill="none"/></svg>
        お問い合わせはメールで
      </p>
      <p class="mail">info@hoshizora-ws.jp</p>
    </div>
    <div class="organizers">
      <p>主催：みさきショッピングパークLumo</p>
      <p>運営協力：株式会社Hoshizora（ホシゾラ）</p>
      <p>後援：岬野市教育委員会</p>
      <div class="brand"><i></i>Hoshizora</div>
    </div>
  </footer>
</main>
</body>
</html>
```